Flyer for language school

Hi,
We are language school, we offre german courses.
We will provide our students with a notepad during registration in a german course.
For that, we need the front page ofthe notepad to be pretty, simple and remarkable.
U can find our colors in the logo in the attachement.
for the contact information, we need those three adresses
Tunis - Imm Les Cyprès, 3ème étage 47 Rue des Mimosas, 2089 Les Jardins du Nord 3
Tél : 71 438 506
Email : tunis@lerbavo.org
Sfax - Imm Yasmina, 5ème étage Rue Karim Bensaid (en face de la rtpm), 3142 Sfax
Tél : 74 815 672
Email : sfax@lerbavo.org
Sousse - 14 Ave Hédi Marzouki (prés du rond point Horizon au dessus du café Mirabelle).
Tél : 73 592 031
Email : sousse@lerbavo.org
The website needs to be cited also :
www.lerbavo.org

```html
<!DOCTYPE html>
<html lang="fr">
<head>
<meta charset="utf-8">
<title>Lerbavo – Notepad cover</title>
<link href="https://fonts.googleapis.com/css2?family=Lato:wght@400;700;900&family=Raleway:wght@400&display=swap" rel="stylesheet">
<style>
  :root{
    --bg:#f7f9f9;
    --paper-top:#ffffff;
    --paper-bottom:#ececee;
    --ink:#1d1d1d;
    --flag-black:#4a4a4c;
    --flag-red:#d62828;
    --flag-gold:#f7c51c;
    --tunis:#f6c21a;
    --sousse:#e02b2b;
    --sfax:#111111;
    --brand:#d4df1e;
  }
  html,body{margin:0;width:1200px;height:1000px;overflow:hidden;background:var(--bg);}
  body{position:relative;font-family:"Lato",sans-serif;color:var(--ink);}
  .cover{
    position:absolute;left:355px;top:108px;width:497px;height:768px;overflow:hidden;
    background:linear-gradient(180deg,var(--paper-top) 0%,#f4f4f5 45%,var(--paper-bottom) 100%);
  }
  .flag-art{position:absolute;left:0;top:0;}
  .brand{position:absolute;left:26px;top:86px;display:flex;align-items:center;gap:8px;}
  .brand-mark{width:14px;height:14px;background:var(--brand);}
  .brand-name{font-weight:900;font-size:30px;color:#2b2b2b;letter-spacing:-0.5px;}
  .office{
    position:absolute;border-radius:50%;background:linear-gradient(160deg,#ffffff,#eeeeef);
    box-shadow:0 4px 14px rgba(0,0,0,.10);display:flex;align-items:center;justify-content:center;
  }
  .office-ring{
    position:absolute;inset:6px;border-radius:50%;border:1.2px solid currentColor;
  }
  .office-body{position:relative;text-align:center;font-size:11px;line-height:15px;color:var(--ink);}
  .office-city{font-weight:900;font-size:34px;line-height:36px;margin-bottom:6px;letter-spacing:.5px;}
  .office--tunis{left:39px;top:212px;width:200px;height:200px;color:var(--tunis);}
  .office--sousse{left:85px;top:387px;width:210px;height:210px;color:var(--sousse);}
  .office--sfax{left:237px;top:494px;width:216px;height:216px;color:var(--sfax);}
  .office--sfax .office-city{font-size:40px;line-height:42px;}
  .website{
    position:absolute;left:0;right:0;top:722px;text-align:center;
    font-family:"Raleway",sans-serif;font-size:22px;letter-spacing:12px;color:#222;padding-left:12px;
  }
</style>
</head>
<body>
  <main class="cover">
    <svg class="flag-art" width="497" height="768" viewBox="0 0 497 768" aria-hidden="true">
      <defs>
        <clipPath id="flag-disc"><circle cx="497" cy="262" r="206"/></clipPath>
        <radialGradient id="halo" cx="0.5" cy="0.5" r="0.5">
          <stop offset="0.85" stop-color="#000" stop-opacity=".10"/>
          <stop offset="1" stop-color="#000" stop-opacity="0"/>
        </radialGradient>
      </defs>
      <circle cx="497" cy="270" r="250" fill="url(#halo)"/>
      <circle cx="497" cy="262" r="232" fill="#fbfbfb" stroke="#111" stroke-width="1.3"/>
      <g clip-path="url(#flag-disc)">
        <rect x="280" y="40" width="230" height="120" fill="var(--flag-black)"/>
        <rect x="280" y="188" width="230" height="146" fill="var(--flag-red)"/>
        <rect x="280" y="364" width="230" height="120" fill="var(--flag-gold)"/>
      </g>
    </svg>

    <div class="brand">
      <span class="brand-mark"></span>
      <span class="brand-name">lerbavo</span>
    </div>

    <section class="office office--tunis">
      <span class="office-ring"></span>
      <div class="office-body">
        <h2 class="office-city" style="margin-top:0">TUNIS</h2>
        Imm Les Cyprès, 3ème étage<br>
        47 Rue des Mimosas,<br>
        2089 Les Jardins du Nord 3<br>
        Tél : 71 438 506<br>
        Email : tunis@lerbavo.org
      </div>
    </section>

    <section class="office office--sousse">
      <span class="office-ring"></span>
      <div class="office-body">
        <h2 class="office-city" style="margin-top:0">SOUSSE</h2>
        14 Ave Hédi Marzouki<br>
        (prés du rond point Horizon<br>
        au dessus du café Mirabelle).<br>
        Tél : 73 592 031<br>
        Email : sousse@lerbavo.org
      </div>
    </section>

    <section class="office office--sfax">
      <span class="office-ring"></span>
      <div class="office-body">
        <h2 class="office-city" style="margin-top:0">SFAX</h2>
        Imm Yasmina, 5ème étage Rue<br>
        Karim Bensaid (en face de la rtpm),<br>
        3142 Sfax<br>
        Tél : 74 815 672<br>
        Email : sfax@lerbavo.org
      </div>
    </section>

    <p class="website">www.lerbavo.org</p>
  </main>
</body>
</html>
```